Modern Innovative Business Card Design

We require a nice, modern, clean business card design, ready for upload to Cardwello. Our company develops online banking software solutions for small financial insitutions. The design should be clean, professional, but yet not "corporate boring". See www.fintrola.com for an idea of business image and profile. The design should communicate innovation, be modern and fresh, yet look professional and established.

Target Market(s)

Finance industry, bankers, entrepreneurs

Industry/Entity Type

Financial

Contact Information for Business Card

Daniel Hargreave
CEO

FINTROLA BV
Lindenhofstraat 38
1072 KD Amsterdam
The Netherlands

Phone: +31 20 517 8063
Direct: +31 20 446 1975
Skype: daniel.fintrola
ceo@fintrola.com
www.fintrola.com

Font styles to use
Sans Serif

Requirements
Must have
• Should look clean, modern and professional. File should be ready for upload to cardwello.
Should not have
• Boring standard corporate layout

```html
<!DOCTYPE html>
<html lang="en">
<head>
<meta charset="utf-8">
<title>Fintrola Business Card</title>
<link rel="stylesheet" href="https://fonts.googleapis.com/css2?family=Cinzel:wght@400;700&display=swap">
<style>
  :root {
    --backdrop: #e4e2de;
    --card-light: #ffffff;
    --card-shade: #e9e9e9;
    --band: #6f6f6f;
    --band-text: #f4f4f4;
    --ink: #5a5a5a;
    --ink-soft: #777777;
    --accent: #8cc63f;
  }
  * { margin: 0; padding: 0; box-sizing: border-box; }
  html, body {
    width: 1200px;
    height: 600px;
    overflow: hidden;
    background: var(--backdrop);
  }
  .canvas {
    position: relative;
    width: 1200px;
    height: 600px;
  }
  .card {
    position: absolute;
    left: 220px;
    top: 85px;
    width: 760px;
    height: 430px;
    background: linear-gradient(115deg, var(--card-shade) 0%, var(--card-light) 45%, var(--card-light) 60%, var(--card-shade) 100%);
    box-shadow: 0 10px 30px rgba(0,0,0,0.18);
    font-family: "Cinzel", Georgia, serif;
    color: var(--ink);
  }
  .brand {
    position: absolute;
    left: 58px;
    top: 96px;
    display: flex;
    align-items: center;
    gap: 14px;
  }
  .brand-square {
    width: 22px;
    height: 22px;
    background: var(--accent);
  }
  .brand-name {
    font-size: 62px;
    font-weight: 400;
    letter-spacing: 3px;
    color: var(--ink);
    line-height: 1;
  }
  .band {
    position: absolute;
    left: 0;
    top: 212px;
    width: 100%;
    height: 66px;
    background: var(--band);
  }
  .holder {
    position: absolute;
    left: 58px;
    top: 12px;
    color: var(--band-text);
  }
  .holder-name {
    font-size: 22px;
    font-weight: 700;
    letter-spacing: 1px;
    line-height: 1.1;
  }
  .holder-role {
    font-size: 14px;
    letter-spacing: 1px;
    margin-top: 3px;
  }
  .contacts {
    position: absolute;
    left: 58px;
    top: 298px;
    list-style: none;
  }
  .contacts li {
    display: flex;
    align-items: center;
    gap: 10px;
    font-size: 14px;
    line-height: 21px;
    color: var(--ink-soft);
  }
  .contacts svg { width: 13px; height: 13px; flex: none; }
  .address {
    position: absolute;
    left: 440px;
    top: 298px;
    font-size: 16px;
    line-height: 24px;
    color: var(--ink-soft);
    font-style: normal;
  }
</style>
</head>
<body>
<div class="canvas">
  <section class="card">
    <div class="brand">
      <span class="brand-square"></span>
      <span class="brand-name">FINTROLA</span>
    </div>

    <div class="band">
      <div class="holder">
        <div class="holder-name">Daniel Hargreave</div>
        <div class="holder-role">CEO</div>
      </div>
    </div>

    <ul class="contacts">
      <li>
        <svg viewBox="0 0 13 13" aria-hidden="true"><rect x="0.75" y="0.75" width="11.5" height="11.5" rx="2" fill="none" stroke="#8cc63f" stroke-width="1.5"/><path d="M4 3.5 L5.5 3.5 L6 5 L5.2 5.7 Q6 7.3 7.3 7.8 L8 7 L9.5 7.5 L9.5 9 Q6.5 9.5 4.5 6.5 Q3.6 5 4 3.5Z" fill="#8cc63f"/></svg>
        +31 20 517 8063
      </li>
      <li>
        <svg viewBox="0 0 13 13" aria-hidden="true"><rect x="0.75" y="0.75" width="11.5" height="11.5" rx="2" fill="none" stroke="#8cc63f" stroke-width="1.5"/><rect x="4.5" y="3" width="4" height="7" rx="0.8" fill="#8cc63f"/></svg>
        +31 20 446 1975
      </li>
      <li>
        <svg viewBox="0 0 13 13" aria-hidden="true"><rect x="0.75" y="0.75" width="11.5" height="11.5" rx="2" fill="none" stroke="#8cc63f" stroke-width="1.5"/><rect x="3" y="4" width="7" height="5" fill="none" stroke="#8cc63f" stroke-width="1"/><path d="M3 4 L6.5 7 L10 4" fill="none" stroke="#8cc63f" stroke-width="1"/></svg>
        ceo@fintrola.com
      </li>
      <li>
        <svg viewBox="0 0 13 13" aria-hidden="true"><rect x="0.75" y="0.75" width="11.5" height="11.5" rx="2" fill="none" stroke="#8cc63f" stroke-width="1.5"/><circle cx="6.5" cy="6.5" r="3" fill="none" stroke="#8cc63f" stroke-width="1"/><path d="M3.5 6.5 H9.5 M6.5 3.5 V9.5" stroke="#8cc63f" stroke-width="0.8"/></svg>
        www.fintrola.com
      </li>
      <li>
        <svg viewBox="0 0 13 13" aria-hidden="true"><rect x="0.75" y="0.75" width="11.5" height="11.5" rx="2" fill="none" stroke="#8cc63f" stroke-width="1.5"/><path d="M3.5 4 H9.5 V8 H6 L4.5 9.5 V8 H3.5Z" fill="#8cc63f"/></svg>
        daniel.fintrola
      </li>
    </ul>

    <address class="address">
      Lindenhofstraat 38, 1072 KD<br>
      Amsterdam The Netherlands
    </address>
  </section>
</div>
</body>
</html>
```